I need a business card design for my youtube channel called The Brisk Kettle Corner. I make youtube cooking tutorials. I'd like the phrase " I'll see you next time, for my next meal" somewhere on the BC. The Youtube web address is www.vidloom.example/user/BriskKettleCorner
email - booking@harlowvane.example

Target Market(s)

This is for companies & business opportunities so it needs to look professional & sleek.

Industry/Entity Type

Cooking

Requirements
Must have
• Must have my Brisk kettle corner logo on the card preferably top left. My name ( Marcus Ellery ). Name of my channel "Brisk Kettle Corner" & the yoube logo & web address for my channel & the email booking@harlowvane.example & the 3 pics of food.

```html
<!DOCTYPE html>
<html lang="en">
<head>
<meta charset="utf-8">
<title>The Brisk Kettle Corner – Business Card</title>
<link rel="stylesheet" href="https://fonts.googleapis.com/css2?family=Arimo:wght@400;700&family=Gochi+Hand&display=swap">
<style>
  :root {
    --ink: #0b0b0b;
    --orange: #f7a21b;
    --white: #ffffff;
    --paper: #ecebe8;
  }
  * { box-sizing: border-box; margin: 0; padding: 0; }
  html, body { width: 1200px; height: 900px; overflow: hidden; }
  body {
    background: var(--paper);
    font-family: "Arimo", Arial, sans-serif;
    position: relative;
  }
  .card {
    position: absolute;
    left: 250px;
    width: 700px;
    height: 400px;
    overflow: hidden;
    box-shadow: 0 6px 18px rgba(0,0,0,.18);
  }
  /* Back side */
  .card--back { top: 30px; background: var(--ink); }
  .back-brand {
    position: absolute;
    left: 50%; top: 50%;
    transform: translate(-50%, -50%);
    display: flex; align-items: center; gap: 18px;
  }
  .back-brand__dot {
    width: 44px; height: 44px; border-radius: 50%; background: var(--orange);
  }
  .back-brand__name {
    color: var(--orange); font-weight: 700; font-size: 30px; white-space: nowrap;
  }
  /* Front side */
  .card--front { top: 470px; background: var(--white); }
  .front-head {
    position: absolute; left: 0; top: 0; width: 100%; height: 185px;
    background: var(--ink);
  }
  .front-brand {
    position: absolute; left: 24px; top: 40px; width: 150px;
    display: flex; flex-direction: column; align-items: center; gap: 10px;
  }
  .front-brand__dot {
    width: 60px; height: 60px; border-radius: 50%; background: var(--orange);
  }
  .front-brand__name {
    color: var(--orange); font-weight: 700; font-size: 12px; white-space: nowrap;
  }
  .identity { position: absolute; left: 200px; top: 66px; }
  .identity__line { display: flex; align-items: baseline; gap: 10px; }
  .identity__name { color: var(--orange); font-weight: 700; font-size: 27px; white-space: nowrap; }
  .identity__channel {
    color: var(--white); font-size: 15px; text-transform: uppercase; letter-spacing: .3px; white-space: nowrap;
  }
  .identity__tagline {
    font-family: "Gochi Hand", cursive; color: var(--orange); font-size: 21px; margin-top: 6px; white-space: nowrap;
  }
  .gallery {
    position: absolute; left: 0; top: 185px; width: 100%; height: 140px;
    background: var(--orange);
    display: flex; gap: 8px; padding-top: 6px;
  }
  .gallery__cell { flex: 1; background: var(--white); padding: 8px 10px; }
  .gallery__photo { width: 100%; height: 100%; }
  .photo--pool-cake { background: linear-gradient(160deg, #efe07a, #e6d25a); }
  .photo--candy-cake { background: linear-gradient(160deg, #c95a3e, #7a4f33); }
  .photo--layered-jelly { background: linear-gradient(160deg, #d0563f, #4f86b8); }
  .contact-band {
    position: absolute; left: 0; bottom: 0; width: 100%; height: 75px;
    background: var(--orange);
    display: flex; align-items: center; justify-content: space-between;
    padding: 0 28px 0 22px;
    color: var(--ink); font-size: 19px;
  }
  .contact { display: flex; align-items: center; gap: 10px; white-space: nowrap; }
  .contact__badge {
    width: 28px; height: 28px; border-radius: 50%; background: var(--ink);
    display: flex; align-items: center; justify-content: center;
  }
</style>
</head>
<body>
  <section class="card card--back" aria-label="Card back">
    <div class="back-brand">
      <span class="back-brand__dot" aria-hidden="true"></span>
      <span class="back-brand__name">The Brisk Kettle Corner</span>
    </div>
  </section>

  <section class="card card--front" aria-label="Card front">
    <header class="front-head">
      <div class="front-brand">
        <span class="front-brand__dot" aria-hidden="true"></span>
        <span class="front-brand__name">The Brisk Kettle Corner</span>
      </div>
      <div class="identity">
        <div class="identity__line">
          <span class="identity__name">Marcus Ellery</span>
          <span class="identity__channel">Brisk Kettle Corner</span>
        </div>
        <p class="identity__tagline">I'll see you next time, for my next meal.</p>
      </div>
    </header>

    <div class="gallery">
      <div class="gallery__cell"><div class="gallery__photo photo--pool-cake" role="img" aria-label="Photo of a yellow frosted party cake"></div></div>
      <div class="gallery__cell"><div class="gallery__photo photo--candy-cake" role="img" aria-label="Photo of a candy-covered layer cake sliced open"></div></div>
      <div class="gallery__cell"><div class="gallery__photo photo--layered-jelly" role="img" aria-label="Photo of a multicoloured layered jelly slice"></div></div>
    </div>

    <footer class="contact-band">
      <div class="contact">
        <span class="contact__badge" aria-hidden="true"></span>
        <span>/user/BriskKettleCorner</span>
      </div>
      <div class="contact">
        <span class="contact__badge" aria-hidden="true">
          <svg width="16" height="12" viewBox="0 0 16 12"><rect x="1" y="1" width="14" height="10" fill="none" stroke="#f7a21b" stroke-width="1.5"/><path d="M1 1 L8 7 L15 1" fill="none" stroke="#f7a21b" stroke-width="1.5"/></svg>
        </span>
        <span>booking@harlowvane.example</span>
      </div>
    </footer>
  </section>
</body>
</html>
```